Company or website name
- BrightPenny
- Links to the website
- We sell daily deals to users of all ages...Our site uses the power of social media to spread our daily deals
- Other Facts

```html
<!DOCTYPE html>
<html lang="en">
<head>
<meta charset="utf-8">
<title>BrightPenny – Today's Deal</title>
<link rel="stylesheet" href="https://fonts.googleapis.com/css2?family=Arimo:wght@400;700&family=Roboto+Condensed:wght@400;700&display=swap">
<style>
:root{
  --ink:#222;
  --text:#555;
  --muted:#888;
  --blue:#3a9dc6;
  --link-blue:#1d5fa8;
  --orange:#f39a1e;
  --orange-dark:#d9700a;
  --dark:#1f1f1f;
  --nav:#262626;
  --panel:#e6e6e6;
  --panel-side:#b8b8b8;
  --white:#fff;
  --line:#c9c9c9;
  --body-font:"Arimo",Arial,sans-serif;
  --head-font:"Roboto Condensed","Arial Narrow",sans-serif;
}
*{box-sizing:border-box;margin:0;padding:0}
html,body{width:1119px;height:1200px;overflow:hidden;background:var(--white)}
body{position:relative;font-family:var(--body-font);color:var(--text)}
.abs{position:absolute}

/* header */
.header{left:0;top:0;width:1119px;height:148px;background:linear-gradient(#cfcfd2 0,#e9e9ee 45%,#fbfbfd 100%)}
.subscribe-tab{left:220px;top:27px;width:672px;height:36px}
.subscribe-tab svg{position:absolute;left:0;top:0}
.subscribe-label{left:22px;top:11px;font-size:13px;color:#666;white-space:nowrap}
.field{background:var(--white);border:1px solid #bbb;border-radius:2px;font-size:11px;color:#333;padding:5px 6px;height:24px;white-space:nowrap}
.city-select{left:172px;top:4px;width:186px}
.city-select::after{content:"";position:absolute;right:6px;top:8px;border:5px solid transparent;border-top:7px solid #333}
.email-field{left:364px;top:4px;width:194px}
.subscribe-btn{left:566px;top:4px;width:72px;height:24px;background:var(--orange);color:var(--white);font-size:9px;font-weight:700;text-align:center;line-height:24px;border-radius:2px}
.close-dot{left:658px;top:2px;width:14px;height:14px;border-radius:50%;background:#ddd;color:#777;font-size:10px;line-height:14px;text-align:center}
.brand{left:146px;top:97px;display:flex;align-items:center;gap:8px}
.brand-dot{width:30px;height:30px;border-radius:50%;background:var(--link-blue)}
.brand-name{font-size:38px;color:var(--link-blue);font-weight:400;letter-spacing:-.5px}

/* nav */
.nav{left:0;top:148px;width:1119px;height:32px;background:var(--nav)}
.nav-item{top:0;height:32px;line-height:32px;color:var(--white);font-size:11px;font-weight:700;white-space:nowrap}
.nav-item.current{left:0;width:255px;padding-left:147px;background:#111;clip-path:polygon(0 0,243px 0,255px 50%,243px 100%,0 100%)}
.nav-btn{top:6px;height:21px;line-height:21px;padding:0 9px;background:linear-gradient(#9a9a9a,#6f6f6f);color:#ddd;font-size:10px;font-weight:700;border-radius:2px}

/* deal panel */
.deal{left:138px;top:220px;width:850px;height:294px;background:var(--panel);border:1px solid #ccc;border-radius:8px 8px 0 0}
.deal-side{left:638px;top:0;width:211px;height:293px;background:var(--panel-side);border-radius:0 8px 0 0}
.video-frame{left:157px;top:245px;width:399px;height:248px;background:var(--white);box-shadow:0 3px 4px rgba(0,0,0,.25)}
.video-top{left:9px;top:9px;width:382px;height:27px;background:#2b2b2b}
.video-still{left:9px;top:36px;width:382px;height:196px;background:linear-gradient(135deg,#6a5a4e,#2f7bc0 55%,#3a3a3a)}
.video-controls{left:9px;top:232px;width:382px;height:14px;background:#eee;border-top:2px solid #c33}
.refer{left:252px;top:236px;width:171px;height:23px;background:var(--white);border:1px solid #ccc;border-radius:12px;font-size:11px;font-weight:700;color:var(--ink);text-align:center;line-height:21px;box-shadow:0 1px 2px rgba(0,0,0,.2)}
.refer b{color:#d11}
.deal-title{left:559px;top:263px;font-family:var(--head-font);font-size:21px;font-weight:700;color:var(--ink)}
.deal-summary{left:559px;top:300px;width:186px;font-size:12.5px;line-height:18.5px;color:#666}
.stars{left:559px;top:411px;font-size:19px;color:var(--orange);letter-spacing:1px}
.highlights{left:561px;top:437px;font-size:10.5px;line-height:14px;color:var(--link-blue);list-style:none}
.highlights li::before{content:"» ";font-weight:700}

.price-box{left:793px;top:229px;width:177px;height:73px;background:#777;color:var(--white);font-family:var(--head-font);font-weight:700;font-size:14px}
.price-row{display:flex;justify-content:space-between;padding:0 16px}
.price-row:first-child{padding-top:5px}
.price-row.save{position:absolute;left:0;bottom:0;width:100%;height:25px;line-height:25px;background:var(--orange);font-size:16px}
.buy{left:764px;top:313px;width:242px;height:57px}
.buy svg{position:absolute;left:0;top:0}
.buy-price{left:27px;top:11px;width:62px;height:34px;border-radius:17px;background:var(--orange-dark);color:var(--white);font-family:var(--head-font);font-weight:700;font-size:24px;text-align:center;line-height:34px}
.buy-label{left:110px;top:4px;color:var(--white);font-family:var(--head-font);font-weight:700;font-size:40px;line-height:48px}
.time-label{left:793px;top:380px;width:180px;text-align:center;font-family:var(--head-font);font-size:17px;color:var(--ink)}
.clock{left:801px;top:406px}
.timer{left:830px;top:405px;display:flex;gap:6px}
.timer span{width:41px;height:33px;background:linear-gradient(#f4f4f4,#cfcfcf);border:1px solid #999;border-radius:4px;text-align:center;line-height:31px;font-size:20px;color:#333}
.bought{left:819px;top:462px;width:141px;height:35px;background:linear-gradient(#a9a9a9,#8c8c8c);border:1px solid #666;border-radius:4px;text-align:center;line-height:33px;font-family:var(--head-font);font-weight:700;font-size:13px;color:#444}

/* share bar */
.share-bar{left:136px;top:515px;width:858px;height:47px;background:linear-gradient(#333,#1c1c1c);border-radius:0 0 4px 4px;color:#eee;font-size:11.5px}
.share-bar .abs{top:14px;white-space:nowrap}
.share-input{left:133px;top:13px !important;width:111px;height:20px;background:var(--white);color:#666;padding:3px 5px;font-size:11px}
.share-send{left:253px;top:14px !important;width:39px;height:18px;background:#ddd;color:#222;text-align:center;line-height:18px;font-size:11px;border-radius:2px}
.social{left:514px;top:15px !important;display:flex;gap:5px}
.social i{width:17px;height:17px;border-radius:3px;display:block}
.thumb{left:645px;top:10px !important;width:26px;height:26px;border-radius:3px;background:#6d84b4}
.like-sq{left:684px;top:16px !important;width:13px;height:13px;background:#3b5998}
.like-text{left:700px}
.share-shadow{left:155px;top:562px;width:820px;height:12px;background:linear-gradient(#bbb,transparent)}

/* tabs */
.tabs-box{left:138px;top:582px;width:855px;height:405px;background:var(--white);border:1px solid #bbb;box-shadow:2px 3px 5px rgba(0,0,0,.3)}
.tab{top:0;height:29px;line-height:29px;text-align:center;font-size:15px;font-weight:700;color:#555;background:linear-gradient(#c9c9c9,#9d9d9d);border-right:1px solid #888}
.tab.active{background:var(--white);color:var(--blue);text-align:left;padding-left:11px}
.about-title{left:39px;top:70px;font-size:16px;font-weight:700;color:var(--blue)}
.about-text{left:40px;top:99px;width:712px;font-size:12.4px;line-height:16.4px;color:#555}
.about-text p{margin-bottom:16px}
.about-text p+p+p{margin-top:16px}

/* footer */
.footer{left:0;top:1014px;width:1119px;height:186px;background:#2a2a2a}
.footer-low{left:0;top:1134px;width:1119px;height:66px;background:#1e1e1e}
.footer-col{top:1031px;font-size:12px;color:#aaa}
.footer-col h3{font-weight:400;font-size:12px;color:#999;margin-bottom:10px}
.footer-col ul{list-style:none;padding-left:3px}
.footer-col li{line-height:18px}
.follow li{display:flex;align-items:center;gap:9px;font-size:10px;font-weight:700;line-height:22px}
.follow i{width:17px;height:17px;border-radius:2px;display:block}
.support{left:746px;top:1030px;width:202px;height:72px;background:#444;color:#eee;padding:7px 8px}
.support h3{font-family:var(--head-font);font-size:15px;margin-bottom:5px;padding-left:6px}
.support p{font-size:10px;line-height:14px}
</style>
</head>
<body>

<header class="abs header">
  <div class="abs subscribe-tab">
    <svg width="672" height="36" viewBox="0 0 672 36"><polygon points="0,0 672,0 657,36 15,36" fill="#c6c6c9"/></svg>
    <span class="abs subscribe-label">Get the Daily deals for :</span>
    <div class="abs field city-select">Lorem Ipsum is simply dummy</div>
    <div class="abs field email-field">Enter Email Address</div>
    <div class="abs subscribe-btn">SUBSCRIBE</div>
    <div class="abs close-dot">×</div>
  </div>
  <div class="abs brand"><span class="brand-dot"></span><span class="brand-name">BrightPenny</span></div>
</header>

<nav class="abs nav">
  <span class="abs nav-item current">TODAY'S DEAL</span>
  <span class="abs nav-item" style="left:270px">PREVIOUS DEALS</span>
  <span class="abs nav-item" style="left:396px">HOW DOES IT WORK?</span>
  <span class="abs nav-btn" style="left:988px">Sign in</span>
  <span class="abs nav-btn" style="left:1045px">Register</span>
</nav>

<section class="abs deal">
  <div class="abs deal-side"></div>
</section>

<div class="abs video-frame">
  <div class="abs video-top"></div>
  <div class="abs video-still" role="img" aria-label="Deal video still: a man in a blue t-shirt trying on sunglasses"></div>
  <div class="abs video-controls"></div>
</div>
<div class="abs refer">Refer aFriend, Get <b>$10</b></div>

<h1 class="abs deal-title">Looping Adventure!</h1>
<p class="abs deal-summary">Lorem Ipsum is simply dummy text of the printing and typesetting industry. Lorem Ipsum has been the industry's standard dummy text ever since the 1500s,</p>
<div class="abs stars">★★★★★</div>
<ul class="abs highlights">
  <li>Lorem Ipsum is simply</li>
  <li>dummy text of the</li>
  <li>printing and typesetting industry.</li>
</ul>

<div class="abs price-box">
  <div class="price-row"><span>Value</span><span>$44.00</span></div>
  <div class="price-row"><span>Discount</span><span>70%</span></div>
  <div class="price-row save"><span>You Save</span><span>$31.00</span></div>
</div>

<div class="abs buy">
  <svg width="242" height="57" viewBox="0 0 242 57">
    <polygon points="18,0 242,0 242,57 18,57 0,28" fill="#f39a1e"/>
    <polygon points="18,0 242,0 242,4 16,4" fill="#f7b552"/>
  </svg>
  <div class="abs buy-price">$50</div>
  <div class="abs buy-label">BUY!</div>
</div>

<div class="abs time-label">Time Left for this Deal</div>
<svg class="abs clock" width="31" height="31" viewBox="0 0 31 31">
  <circle cx="15.5" cy="15.5" r="14" fill="#2a8fd6" stroke="#fff" stroke-width="2"/>
  <circle cx="15.5" cy="15.5" r="9" fill="none" stroke="#fff" stroke-width="1.5"/>
  <path d="M15.5 9v7h5" fill="none" stroke="#fff" stroke-width="2" stroke-linecap="round"/>
</svg>
<div class="abs timer"><span>14</span><span>06</span><span>33</span></div>
<div class="abs bought">1,997 Bought</div>

<div class="abs share-shadow"></div>
<div class="abs share-bar">
  <span class="abs" style="left:57px">Tell a friend:</span>
  <div class="abs share-input">Your email</div>
  <div class="abs share-send">send</div>
  <span class="abs" style="left:329px">Share this deal with your friend</span>
  <div class="abs social">
    <i style="background:#4aa3df"></i><i style="background:#3b5998"></i><i style="background:#1b6fa8"></i><i style="background:#f26522"></i>
  </div>
  <div class="abs thumb"></div>
  <div class="abs like-sq"></div>
  <span class="abs like-text">40,206 people like this</span>
</div>

<section class="abs tabs-box">
  <div class="abs tab active" style="left:0;width:117px">Description</div>
  <div class="abs tab" style="left:117px;width:190px">Location</div>
  <div class="abs tab" style="left:309px;width:204px">Review</div>
  <h2 class="abs about-title">About This Deal</h2>
  <div class="abs about-text">
    <p>Lorem Ipsum is simply dummy text of the printing and typesetting industry. Lorem Ipsum has been the industry's standard dummy text ever since the 1500s, when an unknown printer took a galley of type and scrambled it to make a type specimen book. It has survived not only five centuries, but also the leap into electronic typesetting, remaining essentially unchanged. It was popularised in the 1960s with the release of Lettrex sheets containing Lorem Ipsum passages, and more recently with desktop publishing software like Pagecraft Studio including versions of Lorem Ipsum.</p>
    <p>It is a long established fact that a reader will be distracted by the readable content of a page when looking at its layout. The point of using Lorem Ipsum is that it has a more-or-less normal distribution of letters, as opposed to using 'Content here, content here', making it look like readable English. Many desktop publis</p>
    <p>It is a long established fact that a reader will be distracted by the readable content of a page when looking at its layout. The point of using Lorem Ipsum is that it has a more-or-less normal distribution of letters, as opposed to using 'Content here, content here', making it look like readable English. Many desktop publis</p>
  </div>
</section>

<footer>
  <div class="abs footer"></div>
  <div class="abs footer-low"></div>
  <div class="abs footer-col" style="left:144px">
    <h3>Company</h3>
    <ul><li>Home</li><li>Contact Us</li><li>About BrightPenny</li><li>Jobs at BrightPenny</li></ul>
  </div>
  <div class="abs footer-col" style="left:333px">
    <h3>Get Involved</h3>
    <ul><li>FAQ</li><li>Affiliate Program</li><li>Suggest a Business</li><li>Get Featured</li></ul>
  </div>
  <div class="abs footer-col follow" style="left:553px">
    <h3>Follow Us</h3>
    <ul>
      <li><i style="background:#4aa3df"></i>Follow us</li>
      <li><i style="background:#3b5998"></i>Follow us</li>
      <li><i style="background:#1b6fa8"></i>Follow us</li>
    </ul>
  </div>
  <div class="abs support">
    <h3>Questions and Support</h3>
    <p>Lorem Ipsum is simply dummy FAQs. the printing and typesetting industry.</p>
  </div>
</footer>

</body>
</html>
```